Zielgruppe
Wir vermarkten steirische Produkte. Bei diesem Projekt geht es um unser mehrfach Kürbiskernöl. Unser Steirisches Kürbiskernöl ist seit vielen Jahren prämiert, 100% rein, frei von Zusatzstoffen und wird bei uns am Hof, in der eigenen Ölmühle, laufend frisch gepresst.
Wir sind ein Familienbetrieb und legen viel Wert auf die Qualität unserer Produkte.
Für weitere Informationen besuchen Sie am besten unsere Homepage www.saatgoldhaus.at oder Facebookseite 'Ferien- & Wiesenhof Trattnig'
Aufgabenstellung
Im Fotomaterial sehen sie auch unser derzeitiges Kürbiskernöl-Etikett. Bitte beachten Sie, dass die Banderole als auch die Goldprämierung zum neuen Etikett passen sollten. Zudem bitte das Design von der 'Samtbaronin' beachten, auch das Kürbiskernöl Etikett sollte modern sein und zu der Samtbaronin passen. Zudem hätten wir gerne unser Logo (auch anbei) im Etikett.
Weiters hätten wir gerne ein Etikett für unsere 'Kürbiskerne', welches das gleiche Design wie das Kernöletikett hat. Folgende Anpassungen bei den Angaben: Kürbiskerne, Name/Kontaktdaten gleich/, Vor Licht geschützt und trocken lagern. Freifeld für Datum nach Mindestens haltbar bis sowie Angabe von natur/geröstet/gesalzen.
Am Kernöletikett- Etikett anzugeben sind folgende Informationen.
Nettofüllmenge (0,25l/0,5l,1l) – je nach Füllmenge sollte das Etikett von der Größe variieren (Nettofüllmenge Mindestschriftgröße 4mm)
Mindestschriftgröße folgender Angaben: 1,2mm
Kürbiskernöl
Fam. Trattnig
Lindengrund 12
8490 Bad Radkersburg
www.saatgoldhaus.at
Mindestens haltbar bis: - danach ein Freifeld, damit wir das Datum darauf drücken können
Vor Wärme und Licht geschützt lagern
Nach dem Öffnen gut verschlossen aufbewahren und zügig verbrauchen.
100ml enthalten durchschnittlich
Energie 3404kJ / 828 kcal
Fett 92g
davon: gesättigte Fettsäuren 17g
Enthält geringfügige Mengen von Kohlenhydraten, Zucker, Eiweiß und Salz.

```html
<!DOCTYPE html>
<html lang="de">
<head>
<meta charset="utf-8">
<title>Kürbiskernöl Etikett – Fam. Trattnig</title>
<link rel="stylesheet" href="https://fonts.googleapis.com/css2?family=PT+Sans+Narrow&family=Questrial&display=swap">
<style>
  :root {
    --green-deep: #03251a;
    --green-mid: #0b4a2c;
    --green-light: #146038;
    --gold-dark: #a8843e;
    --gold: #c9a75a;
    --gold-light: #f1e3a6;
    --text-light: #e4e8e2;
    --white: #ffffff;
  }
  * { margin: 0; padding: 0; box-sizing: border-box; }
  html, body { width: 1200px; height: 960px; overflow: hidden; background: var(--green-deep); }
  .label {
    position: relative;
    width: 1200px; height: 960px;
    background:
      radial-gradient(ellipse 70% 80% at 55% 45%, var(--green-light) 0%, var(--green-mid) 40%, var(--green-deep) 100%);
    font-family: "PT Sans Narrow", "Arial Narrow", sans-serif;
    color: var(--text-light);
    overflow: hidden;
  }
  .gold-band {
    position: absolute; left: 0; top: 18px; width: 1200px; height: 15px;
    background: linear-gradient(90deg, var(--gold-dark) 0%, var(--gold) 40%, var(--gold-light) 50%, var(--gold) 58%, var(--gold-dark) 100%);
  }
  .info {
    position: absolute;
    font-size: 27px; line-height: 40.5px;
  }
  .storage { left: 32px; top: 112px; }
  .nutrition { left: 871px; top: 104px; }
  .address { left: 32px; top: 590px; }
  .product-name {
    position: absolute; left: 382px; top: 78px; height: 630px;
    writing-mode: vertical-rl; transform: rotate(180deg);
    font-family: "Questrial", "Century Gothic", sans-serif;
    font-size: 86px; line-height: 90px; letter-spacing: 1px;
    color: var(--white); text-align: center;
  }
  .origin {
    position: absolute; left: 548px; top: 132px;
    font-family: "Questrial", "Century Gothic", sans-serif;
    font-size: 35px; line-height: 46px;
    color: var(--gold);
  }
  .pumpkin-art {
    position: absolute; left: 490px; top: 375px; width: 300px; height: 330px;
  }
  .net-quantity {
    position: absolute; left: 868px; top: 560px; width: 250px; text-align: center;
    color: var(--gold-light);
  }
  .net-quantity .caption { font-size: 38px; line-height: 46px; color: var(--gold); }
  .net-quantity .amount { font-size: 46px; line-height: 60px; margin-top: 10px; }
  .brand {
    position: absolute; left: 420px; top: 780px; width: 360px; text-align: center;
    font-family: "Questrial", "Century Gothic", sans-serif;
    color: var(--white);
  }
  .brand .brand-name { font-size: 58px; letter-spacing: 3px; line-height: 66px; }
  .brand .brand-sub { font-size: 30px; line-height: 40px; margin-top: 12px; }
  .shipping {
    position: absolute; left: 32px; top: 834px;
    display: flex; align-items: flex-start; gap: 16px;
    font-size: 28px; line-height: 38px; color: var(--white);
  }
  .shipping svg { margin-top: 6px; }
  .best-before {
    position: absolute; left: 944px; top: 790px;
    font-size: 27px; line-height: 34px;
  }
  .date-field {
    position: absolute; left: 943px; top: 845px; width: 240px; height: 85px;
    background: var(--white);
  }
</style>
</head>
<body>
<div class="label">
  <div class="gold-band"></div>

  <div class="info storage">
    Vor Wärme und Licht<br>geschützt lagern.<br>Nach dem Öffnen<br>gut verschlossen<br>aufbewahren und<br>zügig verbrauchen.
  </div>

  <h1 class="product-name">KÜRBISKERNÖL</h1>

  <div class="origin">aus der<br>hofeigenen<br>Ölmühle</div>

  <svg class="pumpkin-art" role="img" aria-label="Goldene Kürbis-Illustration" viewBox="0 0 300 330">
    <defs>
      <linearGradient id="pumpkinGold" x1="0" y1="0" x2="1" y2="1">
        <stop offset="0" stop-color="#d6c889"/>
        <stop offset="0.5" stop-color="#9c8c45"/>
        <stop offset="1" stop-color="#5e5524"/>
      </linearGradient>
    </defs>
    <ellipse cx="150" cy="205" rx="145" ry="120" fill="url(#pumpkinGold)"/>
  </svg>

  <div class="info nutrition">
    100ml enthalten<br>durchschnittlich:<br>Energie 3404kJ / 828 kcal<br>Fett 92g&nbsp; davon:<br>gesättigte&nbsp; Fettsäuren 17g<br>Enthält geringfügige<br>Mengen von Kohlenhydraten,<br>Zucker,&nbsp; Eiweiß und Salz.
  </div>

  <div class="net-quantity">
    <div class="caption">Nettofüllmenge</div>
    <div class="amount">0,25 l</div>
  </div>

  <div class="info address">
    Fam. Trattnig<br>Lindengrund 12<br>8490 Bad Radkersburg<br>www.saatgoldhaus.at<br>Tel.: 03476 -&nbsp; 58 04
  </div>

  <div class="brand">
    <div class="brand-name">TRATTNIG</div>
    <div class="brand-sub">Ferien- &amp; Wiesenhof</div>
  </div>

  <div class="shipping">
    <svg width="56" height="40" viewBox="0 0 56 40" aria-hidden="true">
      <rect x="2" y="2" width="52" height="36" fill="none" stroke="#c9a75a" stroke-width="3"/>
      <polyline points="2,2 28,24 54,2" fill="none" stroke="#c9a75a" stroke-width="3"/>
      <line x1="2" y1="38" x2="22" y2="19" stroke="#c9a75a" stroke-width="3"/>
      <line x1="54" y1="38" x2="34" y2="19" stroke="#c9a75a" stroke-width="3"/>
    </svg>
    <span>Postversand<br>möglich</span>
  </div>

  <div class="info best-before">Mindestens haltbar bis:</div>
  <div class="date-field"></div>
</div>
</body>
</html>
```